Postcard Design Project

Education- charter school- elementary k-6th grades- performing arts integrated in to the core curriculum

Industry/Entity Type

School

```html
<!DOCTYPE html>
<html lang="en">
<head>
<meta charset="utf-8">
<title>Bright Stage Arts Community School – Enrollment Postcard</title>
<link href="https://fonts.googleapis.com/css2?family=Open+Sans:wght@400;600;700&family=Courgette&display=swap" rel="stylesheet">
<style>
  :root {
    --yellow: #f6d21a;
    --purple: #5b2a86;
    --orange: #f39419;
    --ink: #1f1f1f;
    --paper: #ffffff;
    --backdrop: #ecebe8;
    --line-grey: #9a9a9a;
  }
  * { margin: 0; padding: 0; box-sizing: border-box; }
  html, body { width: 978px; height: 1200px; overflow: hidden; }
  body {
    background: var(--backdrop);
    font-family: "Open Sans", Arial, sans-serif;
    color: var(--ink);
    position: relative;
  }
  .postcard {
    position: absolute;
    left: 144px;
    width: 690px;
    height: 470px;
    background: var(--paper);
    overflow: hidden;
    box-shadow: 0 4px 14px rgba(0,0,0,0.25);
  }
  .postcard--front { top: 100px; }
  .postcard--back { top: 622px; }
  .postcard__art { position: absolute; inset: 0; width: 690px; height: 470px; }
  .abs { position: absolute; }

  .school-name {
    color: var(--purple);
    font-weight: 400;
    font-size: 13px;
    white-space: nowrap;
    display: flex;
    align-items: center;
    gap: 8px;
  }
  .school-name__dot {
    width: 14px; height: 14px; border-radius: 50%;
    background: var(--purple);
  }
  .headline {
    color: var(--purple);
    font-weight: 700;
    font-size: 30px;
    letter-spacing: 0.2px;
  }
  .intro {
    font-size: 11.5px;
    line-height: 15px;
    text-align: center;
    width: 270px;
  }
  .website { font-weight: 700; font-size: 15px; color: #333; }
  .cta {
    font-family: "Courgette", cursive;
    color: var(--purple);
    font-size: 26px;
    text-align: center;
    width: 200px;
  }
  .phone {
    color: var(--purple);
    font-weight: 700;
    font-size: 19px;
    display: flex;
    align-items: center;
    gap: 4px;
    white-space: nowrap;
  }
  .phone svg { width: 20px; height: 20px; }
  .urgency {
    font-size: 11.5px;
    line-height: 15px;
    text-align: center;
    width: 300px;
  }
  .back-heading { color: var(--purple); font-weight: 700; font-size: 14px; }
  .back-copy {
    font-size: 11.3px;
    line-height: 14.2px;
    text-align: justify;
    width: 302px;
  }
  .back-copy p + p { margin-top: 14px; }
  .return-address { font-size: 8.5px; line-height: 11.5px; }
  .return-address strong { color: var(--purple); font-weight: 700; display: block; }
  .stamp-box {
    width: 84px; height: 54px;
    border: 1.2px solid var(--line-grey);
  }
</style>
</head>
<body>

<section class="postcard postcard--front">
  <svg class="postcard__art" viewBox="0 0 690 470" aria-hidden="false">
    <defs>
      <linearGradient id="kidsPhotoTones" x1="0" y1="0" x2="1" y2="1">
        <stop offset="0" stop-color="#8fa06a"/>
        <stop offset="0.4" stop-color="#c23a32"/>
        <stop offset="0.75" stop-color="#5a5450"/>
        <stop offset="1" stop-color="#3a3431"/>
      </linearGradient>
      <linearGradient id="pairPhotoTones" x1="0" y1="0" x2="1" y2="1">
        <stop offset="0" stop-color="#6b4a3a"/>
        <stop offset="0.5" stop-color="#d9c2ad"/>
        <stop offset="1" stop-color="#8fb5d9"/>
      </linearGradient>
    </defs>
    <path role="img" aria-label="Photo of three smiling schoolchildren in red and grey uniforms"
          d="M0,0 H254 C320,70 356,180 340,370 L0,370 Z" fill="url(#kidsPhotoTones)"/>
    <path d="M254,0 C320,70 356,180 340,370" fill="none" stroke="var(--orange)" stroke-width="16"/>
    <path d="M276,0 C340,70 374,180 358,370" fill="none" stroke="var(--purple)" stroke-width="1.6"/>
    <path d="M284,0 C348,70 382,180 366,370" fill="none" stroke="var(--purple)" stroke-width="1.6"/>
    <rect x="346" y="161" width="344" height="80" fill="var(--yellow)"/>
    <path d="M0,356 C200,336 420,404 690,358 L690,470 L0,470 Z" fill="var(--yellow)"/>
    <path d="M0,364 C200,344 420,412 690,366" fill="none" stroke="#fff" stroke-width="1.6"/>
    <path d="M0,371 C200,351 420,419 690,373" fill="none" stroke="#fff" stroke-width="1.6"/>
    <circle cx="302" cy="338" r="76" fill="var(--orange)"/>
    <circle role="img" aria-label="Photo of two smiling girls" cx="302" cy="338" r="67" fill="url(#pairPhotoTones)"/>
  </svg>

  <div class="abs school-name" style="left:416px; top:104px;">
    <span class="school-name__dot"></span>Bright Stage Arts Community School
  </div>
  <h1 class="abs headline" style="left:388px; top:180px;">NOW ENROLLING</h1>
  <p class="abs intro" style="left:388px; top:255px;">
    Bright Stage Arts Community School is the most innovative public elementary school program in Central Ohio through integration of the fine and performing arts in all subjects
  </p>
  <p class="abs website" style="left:412px; top:329px;">www.brightstageschool.org</p>
  <p class="abs cta" style="left:425px; top:390px;">Sign Up Now!</p>
  <p class="abs phone" style="left:443px; top:426px;">
    <svg viewBox="0 0 20 20"><circle cx="10" cy="10" r="8.6" fill="none" stroke="currentColor" stroke-width="1.8"/><path d="M7,5.5 L8.6,5.5 L9.3,8 L8.2,9 C8.8,10.4 9.6,11.2 11,11.8 L12,10.7 L14.5,11.4 L14.5,13 C10,13.5 6.5,10 7,5.5 Z" fill="currentColor"/></svg>
    (614) 555-0142
  </p>
  <p class="abs urgency" style="left:14px; top:412px;">
    Classes fill up quickly so<br>call today to ensure your child’s enrollment!
  </p>
</section>

<section class="postcard postcard--back">
  <svg class="postcard__art" viewBox="0 0 690 470">
    <defs>
      <linearGradient id="groupPhotoTones" x1="0" y1="0" x2="1" y2="0">
        <stop offset="0" stop-color="#6f8a4e"/>
        <stop offset="0.35" stop-color="#b33a3a"/>
        <stop offset="0.65" stop-color="#9fb6d8"/>
        <stop offset="1" stop-color="#c9443a"/>
      </linearGradient>
    </defs>
    <path role="img" aria-label="Photo of four schoolchildren walking together outdoors"
          d="M0,0 H348 V132 C240,150 110,140 0,126 Z" fill="url(#groupPhotoTones)"/>
    <path d="M0,126 C110,140 240,150 348,132" fill="none" stroke="var(--orange)" stroke-width="8"/>
    <line x1="392" y1="147" x2="667" y2="147" stroke="var(--line-grey)" stroke-width="1.2"/>
    <line x1="392" y1="185" x2="667" y2="185" stroke="var(--line-grey)" stroke-width="1.2"/>
    <line x1="392" y1="222" x2="667" y2="222" stroke="var(--line-grey)" stroke-width="1.2"/>
    <path d="M0,366 C200,346 420,414 690,368 L690,470 L0,470 Z" fill="var(--yellow)"/>
    <path d="M0,374 C200,354 420,422 690,376" fill="none" stroke="#fff" stroke-width="1.6"/>
    <path d="M0,381 C200,361 420,429 690,383" fill="none" stroke="#fff" stroke-width="1.6"/>
  </svg>

  <div class="abs return-address" style="left:367px; top:17px;">
    <strong>Bright Stage Arts<br>Community School</strong>
    250 Maple Grove Road<br>Columbus, Ohio 43215<br>Phone (614) 555-0142
  </div>
  <div class="abs stamp-box" style="left:583px; top:19px;"></div>

  <h2 class="abs back-heading" style="left:112px; top:161px;">NOW ENROLLING</h2>
  <div class="abs back-copy" style="left:28px; top:190px;">
    <p>All grade levels take visual arts, music, drama, and dance. Small class sizes with Highly Qualified teachers in the core subjects, beautiful facilities with a five acre campus provide for an outdoor learning experience, and a dedicated staff committed to a positive learning environment are just a few reasons that you will be amazed by this performing arts community school.</p>
    <p>Breakfast and lunch are provided at no cost to you! All of this tuition free! Please contact us for a tour of our school.</p>
  </div>

  <div class="abs school-name" style="left:403px; top:320px;">
    <span class="school-name__dot"></span>Bright Stage Arts Community School
  </div>

  <p class="abs cta" style="left:425px; top:397px;">Sign Up Now!</p>
  <p class="abs phone" style="left:443px; top:433px;">
    <svg viewBox="0 0 20 20"><circle cx="10" cy="10" r="8.6" fill="none" stroke="currentColor" stroke-width="1.8"/><path d="M7,5.5 L8.6,5.5 L9.3,8 L8.2,9 C8.8,10.4 9.6,11.2 11,11.8 L12,10.7 L14.5,11.4 L14.5,13 C10,13.5 6.5,10 7,5.5 Z" fill="currentColor"/></svg>
    (614) 555-0142
  </p>
  <p class="abs urgency" style="left:14px; top:419px;">
    Classes fill up quickly so<br>call today to ensure your child’s enrollment!
  </p>
</section>

</body>
</html>
```